Customer Value Leaflet

We need a bi-fold brochure designing, based on the attached PDF wireframes. Our company name is quillbrookery.com (of which the logo is currently being designed). The corporate colour is orange (the exact shade of which we are happy to leave to the designers discretion).

The leaflet will distributed to customer experience experts and marketers so the design needs to be bright, engaging, clean and simple. Design is critical.

```html
<!DOCTYPE html>
<html lang="en">
<head>
<meta charset="utf-8">
<title>Customer Value Leaflet – quillbrookery.com</title>
<link href="https://fonts.googleapis.com/css2?family=Open+Sans:wght@400;600;700&display=swap" rel="stylesheet">
<style>
  :root {
    --orange: #f7931e;
    --panel-light: #d6d6d6;
    --panel-light-edge: #cbcbcb;
    --panel-dark: #bdbdbd;
    --ink: #1a1a1a;
    --white: #ffffff;
    --icon-bg: #ffffff;
    --icon-tone: #8a8a8a;
    --stop-tone: #4a4a4a;
  }
  * { box-sizing: border-box; margin: 0; padding: 0; }
  html, body { width: 1200px; height: 400px; overflow: hidden; }
  body { font-family: "Open Sans", Arial, sans-serif; color: var(--ink); }

  .leaflet { position: relative; width: 1200px; height: 400px; overflow: hidden; }

  .panel { position: absolute; top: 0; height: 400px; }
  .panel--meet { left: 0; width: 400px; background: linear-gradient(var(--panel-light), var(--panel-light-edge)); }
  .panel--journey { left: 400px; width: 402px; background: linear-gradient(var(--panel-light), var(--panel-light-edge)); border-left: 2px solid var(--white); overflow: hidden; }
  .panel--pitch { left: 802px; width: 398px; background: var(--panel-dark); }

  /* Meet panel */
  .tag {
    position: absolute; top: 11px; height: 40px;
    background: var(--orange); color: var(--white);
    font-size: 15px; font-weight: 600; letter-spacing: .3px;
    display: flex; align-items: center; justify-content: center;
  }
  .tag--kim { left: 11px; width: 173px; }
  .tag--kevin { left: 192px; width: 198px; }

  .portrait {
    position: absolute; top: 70px; height: 114px;
    background: linear-gradient(#f4f4f4, #e2e2e2);
  }
  .portrait--kim { left: 50px; width: 91px; }
  .portrait--kevin { left: 219px; width: 78px; }

  .profile {
    position: absolute; top: 196px;
    font-size: 14.5px; line-height: 19.5px; text-align: center;
  }
  .profile--kim { left: 6px; width: 186px; }
  .profile--kevin { left: 196px; width: 190px; }

  /* Journey panel */
  .timeline { position: absolute; left: 172px; top: 6px; width: 50px; height: 340px; }
  .timeline__label {
    position: absolute; left: 197px; color: var(--white);
    font-size: 13px; font-weight: 600; white-space: nowrap;
    transform: translate(-50%, -50%) rotate(-90deg);
  }
  .timeline__label--week { top: 40px; }
  .timeline__label--month { top: 150px; }
  .timeline__label--months { top: 272px; }

  .event {
    position: absolute; font-size: 13px; line-height: 16.5px; text-align: center;
  }
  .event--left { left: 8px; width: 160px; }
  .event--right { left: 226px; width: 170px; }

  .icon {
    position: absolute; width: 62px; height: 60px; background: var(--icon-bg);
    display: flex; align-items: center; justify-content: center;
  }
  .icon--left { left: 57px; }
  .icon--right { left: 282px; }
  .icon--placeholder { background: linear-gradient(#f2f2f2, #dddddd); }
  .icon__fill { width: 42px; height: 42px; border-radius: 50%; background: var(--icon-tone); }
  .icon__fill--stop { border-radius: 8px; background: var(--stop-tone); }

  /* Bottom band */
  .verdict {
    position: absolute; left: 0; top: 343px; width: 802px; height: 57px; z-index: 2;
    background: var(--orange); font-size: 15px;
  }
  .verdict__lead { position: absolute; left: 11px; top: 18px; }
  .verdict__reveal { position: absolute; left: 534px; top: 18px; }

  /* Pitch panel */
  .pitch__hook {
    position: absolute; left: 24px; top: 26px; width: 360px;
    color: var(--white); font-size: 20px; font-weight: 700; line-height: 27px;
  }
  .pitch__hook .highlight { color: var(--orange); text-decoration: underline; }
  .pitch__payoff {
    position: absolute; right: 20px; top: 174px; width: 360px; text-align: right;
    font-size: 22px; font-weight: 700; line-height: 30px;
  }
  .pitch__more {
    position: absolute; left: 0; top: 262px; width: 398px; text-align: center;
    color: var(--white); font-size: 15px;
  }
  .brand-name {
    position: absolute; left: 0; top: 292px; width: 398px; text-align: center;
    font-size: 22px; font-weight: 700; color: var(--ink); letter-spacing: .5px;
  }
  .pitch__url {
    position: absolute; left: 0; top: 352px; width: 398px; text-align: center;
    font-size: 16px; font-weight: 700;
  }
</style>
</head>
<body>
<main class="leaflet">

  <section class="panel panel--meet">
    <div class="tag tag--kim">MEET KIM</div>
    <div class="tag tag--kevin">MEET KEVIN</div>
    <div class="portrait portrait--kim" role="img" aria-label="Illustration of Kim, a customer"></div>
    <div class="portrait portrait--kevin" role="img" aria-label="Illustration of Kevin, a customer"></div>
    <p class="profile profile--kim">Kim has purchased<br>3 items from you over<br>the past 3 months @<br>£109 margin and you<br>acquired her though a<br>Findwell PPC campaign</p>
    <p class="profile profile--kevin">Kevin purchased<br>an item last week @<br>£31 margin and you<br>acquired him though a<br>retargeting campaign</p>
  </section>

  <section class="panel panel--journey">
    <svg class="timeline" viewBox="0 0 50 340" aria-hidden="true">
      <polygon points="10,0 40,0 40,280 50,280 25,338 0,280 10,280" fill="none" stroke="#ffffff" stroke-width="2"/>
      <line x1="10" y1="84" x2="40" y2="84" stroke="#ffffff" stroke-width="2"/>
      <line x1="10" y1="210" x2="40" y2="210" stroke="#ffffff" stroke-width="2"/>
    </svg>
    <span class="timeline__label timeline__label--week">+ 1 WEEK</span>
    <span class="timeline__label timeline__label--month">+ 1 MONTH</span>
    <span class="timeline__label timeline__label--months">+ 6 MONTHS</span>

    <p class="event event--left" style="top:14px">Kim calls you to return<br>an item…</p>
    <div class="icon icon--left icon--placeholder" style="top:58px" role="img" aria-label="Customer service headset icon"><span class="icon__fill"></span></div>
    <p class="event event--left" style="top:130px">places 4 more online<br>orders…</p>
    <div class="icon icon--left" style="top:170px">
      <svg width="48" height="38" viewBox="0 0 50 40" aria-hidden="true">
        <polyline points="2,4 10,4 16,26 42,26 47,10 12,10" fill="none" stroke="#8a8a8a" stroke-width="3" stroke-linejoin="round"/>
        <line x1="20" y1="14" x2="21" y2="22" stroke="#8a8a8a" stroke-width="2"/>
        <line x1="28" y1="14" x2="28" y2="22" stroke="#8a8a8a" stroke-width="2"/>
        <line x1="36" y1="14" x2="35" y2="22" stroke="#8a8a8a" stroke-width="2"/>
        <circle cx="19" cy="34" r="3.5" fill="#8a8a8a"/><circle cx="39" cy="34" r="3.5" fill="#8a8a8a"/>
      </svg>
    </div>
    <p class="event event--left" style="top:228px">then places another<br>order but doesn't come<br>back for a month</p>
    <div class="icon icon--left" style="top:284px" role="img" aria-label="Stop sign icon"><span class="icon__fill icon__fill--stop"></span></div>

    <p class="event event--right" style="top:14px">Kevin makes another<br>purchase…</p>
    <div class="icon icon--right" style="top:58px">
      <svg width="44" height="36" viewBox="0 0 46 38" aria-hidden="true">
        <path d="M14 14 L20 3 M32 14 L26 3" stroke="#8a8a8a" stroke-width="3" fill="none" stroke-linecap="round"/>
        <rect x="2" y="13" width="42" height="6" fill="#8a8a8a"/>
        <path d="M6 21 H40 L36 36 H10 Z" fill="#8a8a8a"/>
      </svg>
    </div>
    <p class="event event--right" style="top:120px">then 2 more (and even<br>posts about how<br>great your service is)…</p>
    <div class="icon icon--right icon--placeholder" style="top:174px" role="img" aria-label="Social media sharing icon"><span class="icon__fill"></span></div>
    <p class="event event--right" style="top:228px">and continues to make<br>purchases on a<br>bi-monthly basis</p>
    <div class="icon icon--right" style="top:280px">
      <svg width="48" height="38" viewBox="0 0 50 40" aria-hidden="true">
        <polyline points="2,4 10,4 16,26 42,26 47,10 12,10" fill="none" stroke="#8a8a8a" stroke-width="3" stroke-linejoin="round"/>
        <line x1="20" y1="14" x2="21" y2="22" stroke="#8a8a8a" stroke-width="2"/>
        <line x1="28" y1="14" x2="28" y2="22" stroke="#8a8a8a" stroke-width="2"/>
        <line x1="36" y1="14" x2="35" y2="22" stroke="#8a8a8a" stroke-width="2"/>
        <circle cx="19" cy="34" r="3.5" fill="#8a8a8a"/><circle cx="39" cy="34" r="3.5" fill="#8a8a8a"/>
      </svg>
    </div>
  </section>

  <div class="verdict">
    <span class="verdict__lead">Right now you probably think Kim is your best customer…</span>
    <span class="verdict__reveal">but really it is Kevin.</span>
  </div>

  <section class="panel panel--pitch">
    <h1 class="pitch__hook">By predicting <span class="highlight">Customer Lifetime Value</span> today…</h1>
    <p class="pitch__payoff">…you can optimise<br>your business for tomorrow</p>
    <p class="pitch__more">Find our more at</p>
    <p class="brand-name">quillbrookery</p>
    <p class="pitch__url">www.quillbrookery.com</p>
  </section>

</main>
</body>
</html>
```